Coastal Bright Sweep Business Card

We are a cleaning and waste management company with the slogan "making waste to landfill a thing of the past". We would like a re-design of our current business card. On the front we want to continue to use our logo as the focus point. On the back, we want the whole thing re-done to be less busy. We want the staff member’s name, the job title, mobile number, email and website. We do not want the address on the card. We still want the green, black and blue colours used, but a new font for the information on the back. Please do not change the logo design at all. We are also thinking about using icons to replace the text ‘mobile, email, website’. The “events + commercial” banner needs to be incorporated somewhere and needs to read “events + commercial + waste”. Another important point for consideration is that we are very concerned about being environmentally sustainable and will be printing on recycled paper. All designs should be made to compliment this in regards to boldness and colouring. Please find attached our logo, our colour chart and an image of our current business card.

```html
<!DOCTYPE html>
<html lang="en">
<head>
<meta charset="utf-8">
<title>Coastal Bright Sweep Business Card</title>
<link rel="stylesheet" href="https://fonts.googleapis.com/css2?family=Lato:ital,wght@0,400;0,700;0,900;1,400;1,700&display=swap">
<style>
  :root {
    --backdrop: #3a3a3a;
    --brand-blue: #00aeef;
    --brand-green: #7dc242;
    --brand-navy: #1c3f6e;
    --paper: #ebe9e3;
    --ink: #1b1b1b;
    --white: #ffffff;
  }
  * { box-sizing: border-box; margin: 0; padding: 0; }
  html, body {
    width: 1200px; height: 900px; overflow: hidden;
    background: var(--backdrop);
    font-family: "Lato", sans-serif;
  }
  .canvas { position: relative; width: 1200px; height: 900px; }

  .card {
    position: absolute;
    width: 640px; height: 366px;
    overflow: hidden;
    box-shadow: 0 10px 30px rgba(0,0,0,0.45);
  }

  /* Front */
  .card--front {
    left: 470px; top: 56px;
    background: var(--brand-blue);
    color: var(--white);
  }
  .front__brand {
    position: absolute; left: 0; right: 0; top: 70px;
    text-align: center;
    font-weight: 900;
    font-size: 58px;
    line-height: 1.0;
    letter-spacing: 0.5px;
    color: var(--white);
  }
  .front__services {
    position: absolute; left: 0; right: 0; bottom: 48px;
    text-align: center;
    font-weight: 700;
    font-size: 20px;
    letter-spacing: 1px;
    text-transform: uppercase;
  }
  .front__services .plus { color: var(--brand-green); margin: 0 6px; }

  /* Back */
  .card--back {
    left: 90px; top: 478px;
    background: var(--paper);
    color: var(--ink);
  }
  .back__brand {
    position: absolute; right: 44px; top: 40px;
    text-align: left;
    font-weight: 900; font-size: 38px; line-height: 1.0;
    color: var(--brand-blue);
  }
  .back__name {
    position: absolute; left: 44px; top: 100px;
    font-weight: 700; font-size: 27px;
    color: var(--brand-blue);
  }
  .back__title {
    position: absolute; left: 44px; top: 136px;
    font-size: 17px; color: var(--ink);
  }
  .back__rule {
    position: absolute; left: 40px; top: 168px;
    width: 560px; height: 1.5px;
    background: var(--brand-blue);
  }
  .back__contacts {
    position: absolute; left: 44px; top: 184px;
    list-style: none;
    font-size: 17px;
  }
  .back__contacts li { display: flex; align-items: center; gap: 10px; margin-bottom: 8px; }
  .back__contacts svg { width: 14px; height: 14px; fill: var(--brand-blue); flex: none; }
  .back__band { position: absolute; left: 0; bottom: 0; width: 640px; height: 60px; }
  .back__website {
    position: absolute; left: 40px; bottom: 16px;
    font-size: 17px; color: var(--white);
  }
</style>
</head>
<body>
<main class="canvas">

  <section class="card card--front" aria-label="Card front">
    <h1 class="front__brand">Coastal<br>Bright<br>Sweep</h1>
    <p class="front__services">Events<span class="plus">+</span>Commercial<span class="plus">+</span>Waste</p>
  </section>

  <section class="card card--back" aria-label="Card back">
    <h2 class="back__brand">Coastal<br>Bright<br>Sweep</h2>

    <p class="back__name">Jamie Lowden</p>
    <p class="back__title">Client Manager</p>
    <div class="back__rule"></div>

    <ul class="back__contacts">
      <li>
        <svg viewBox="0 0 14 14" aria-hidden="true"><path d="M4 0h6a1 1 0 0 1 1 1v12a1 1 0 0 1-1 1H4a1 1 0 0 1-1-1V1a1 1 0 0 1 1-1zm.5 1.5v9.5h5V1.5z"/></svg>
        0412 555 310
      </li>
      <li>
        <svg viewBox="0 0 14 14" aria-hidden="true"><path d="M0 3h14v8H0z" opacity="0.9"/><path d="M0 3l7 5 7-5" fill="none" stroke="#ebe9e3" stroke-width="1.2"/></svg>
        jlowden@coastalbrightsweep.com.au
      </li>
    </ul>

    <svg class="back__band" viewBox="0 0 640 60" preserveAspectRatio="none" aria-hidden="true">
      <polygon points="0,14 345,14 368,60 0,60" fill="var(--brand-blue)"/>
      <polygon points="358,26 640,26 640,60 376,60" fill="var(--brand-green)"/>
      <polygon points="345,14 352,14 375,60 368,60" fill="var(--white)"/>
    </svg>
    <p class="back__website">www.coastalbrightsweep.com.au</p>
  </section>

</main>
</body>
</html>
```